Beach Volleyball Competition Flyer

Qarin Shore, a beach club in Abu Dhabi, is organising the second volleyball tournament of the year, called Qarin Volleyball Open II. We require a flyer advertising the event, we will need 3 variations of the same design as per the requirements listed below.

The flyer should be fun, with a beach theme and volleyball theme, however it has to be sensitive to the morally conservative nature of the united arab emirates (it can be fun but too edgy).

The flyer should feature the following logos (attached):
Dunmere Regent Hotel
Dunmere Sahel Hotel
Tolvik Harbour Raceway
Fennwood Restaurant and Cafe
Play Orbit
Halcyon Court Dunmere Isle
Marrowgate Azure Dunmere Isle
Gold Moth

I have enclosed our flyer from the previous volleyball classic which was designed in house, as well as several photographs of the event, you can find more in this facebook album (https://www.socialpage.example/media/set/?set=a.918406273551029.4402918377.604718293305617&type=1)

Copy for Flyer Design:

Version 1
QARIN VOLLEYBALL OPEN II
28th September 2013

Do you have what it takes? take part with your team to win cash prizes, stays in Dunmere Isle hotels and other attractions on the Island.

Open bar on selected beverages for players all day.
Register your team of 4 at Qarin Shore by 7pm on 25th September 2013
Only 250 AED per team.
KIK: QARINSHORE
info@qarinshore.example
photogram.example/qarinshore
socialpage.example/qarinshore

Version 2 ---- WITHOUT PLAYORBIT LOGO and MUST BE CROPPED TO 156mm (w) x 185mm (h) without sacrificing the look as this will be printed in a newspaper

QARIN VOLLEYBALL OPEN II
28th September 2013

Only 250 AED per team.
KIK: QARINSHORE
info@qarinshore.example
photogram.example/qarinshore
socialpage.example/qarinshore

Version 3
Qarin Volleyball Open II

the classic is back, are you ready?
Saturday 28th September 2013
KIK: QARINSHORE
info@qarinshore.example
photogram.example/qarinshore
socialpage.example/qarinshore

Target Market(s)

18-40 year olds
seasoned volleyball players
fun loving
sporty
love the beach
love the sea

Industry/Entity Type

Advertising

Requirements
Must have
• beach, sunshine, please only use the photos enclosed or any of the photos of our beach from our instagram or facebook. do not ask me for high quality versions as my computer and phone were recently wiped out!
• Qarin Shore's logo should be prominent, sponsors should be at the bottom and small.
Should not have
• too much nakedness, no pictures of alcohol, pictures should be limited to women wearing regular swim wear (ie. bikini not G-string/thong).
• VERSION 2 of the design SHOULD NOT have the Play Orbit logo.

```html
<!DOCTYPE html>
<html lang="en">
<head>
<meta charset="utf-8">
<title>Qarin Volleyball Open II</title>
<link href="https://fonts.googleapis.com/css2?family=Anton&family=Oswald:wght@500;700&display=swap" rel="stylesheet">
<style>
  :root {
    --red: #d7262c;
    --red-dark: #8e1a1d;
    --orange: #e8892a;
    --yellow: #f5c518;
    --gold-text: #f8d62a;
    --rust: #c4522a;
    --white: #ffffff;
    --ink: #1d1d1d;
    --sponsor: #55565a;
    --sky: #a9cde3;
    --sand: #d9cbb3;
  }
  html, body { margin: 0; padding: 0; overflow: hidden; background: var(--white); }
  .flyer {
    position: relative;
    width: 846px;
    height: 1200px;
    overflow: hidden;
    background: var(--white);
    font-family: "Oswald", "Arial Narrow", sans-serif;
  }
  .beach-photo {
    position: absolute;
    left: 0; top: 250px;
    width: 846px; height: 792px;
    background: linear-gradient(180deg, var(--sky) 0%, #c6dde8 45%, #e6e2d6 62%, var(--sand) 78%, #cbb99c 100%);
  }
  .artwork { position: absolute; left: 0; top: 0; }
  .title-word { font-family: "Anton", "Impact", sans-serif; }
  .slogan, .date-text { font-family: "Oswald", "Arial Narrow", sans-serif; font-weight: 700; }
  .social-bar {
    position: absolute;
    left: 0; top: 1042px;
    width: 846px; height: 38px;
    background: var(--yellow);
    display: flex;
    align-items: center;
    justify-content: center;
    gap: 26px;
  }
  .social-item {
    display: flex; align-items: center; gap: 7px;
    font-weight: 700; font-size: 18px; color: var(--ink);
  }
  .social-mark { width: 22px; height: 22px; background: var(--ink); border-radius: 3px; }
  .sponsors {
    position: absolute;
    left: 0; top: 1080px;
    width: 846px; height: 120px;
    display: flex;
    align-items: center;
    justify-content: space-around;
    padding: 0 14px;
    box-sizing: border-box;
  }
  .sponsor {
    font-family: "Oswald", "Arial Narrow", sans-serif;
    font-weight: 500;
    font-size: 14px;
    line-height: 1.15;
    color: var(--sponsor);
    text-align: center;
    max-width: 88px;
  }
</style>
</head>
<body>
<main class="flyer">
  <div class="beach-photo" role="img" aria-label="Photo of two players leaping at the net during a beach volleyball match, with parasols, loungers and the sea behind"></div>

  <svg class="artwork" width="846" height="1200" viewBox="0 0 846 1200">
    <g class="title-bands" transform="translate(0,200) rotate(-14)">
      <rect class="band band-red" x="-200" y="-500" width="1300" height="500" fill="var(--red)"/>
      <rect class="band band-orange" x="-200" y="0" width="1300" height="112" fill="var(--orange)"/>
      <rect class="band band-yellow" x="-200" y="112" width="1300" height="140" fill="var(--yellow)"/>

      <text class="title-word" x="180" y="-12" font-size="160" fill="var(--white)" textLength="400" lengthAdjust="spacingAndGlyphs">QARIN</text>
      <text class="title-word" x="40" y="98" font-size="88" fill="var(--gold-text)" textLength="740" lengthAdjust="spacingAndGlyphs">VOLLEYBALL</text>
      <text class="title-word" x="40" y="236" font-size="112" fill="var(--rust)" textLength="300" lengthAdjust="spacingAndGlyphs">OPEN</text>

      <g class="edition-badge">
        <circle cx="590" cy="186" r="62" fill="var(--white)"/>
        <circle cx="590" cy="186" r="54" fill="var(--rust)"/>
        <text class="title-word" x="590" y="218" font-size="78" fill="var(--white)" text-anchor="middle">II</text>
      </g>
    </g>

    <g class="slogan" transform="translate(50,648) rotate(-20)" fill="var(--red)">
      <text x="0" y="0" font-size="62">THE CLASSIC IS BACK</text>
      <text x="-4" y="78" font-size="80">ARE YOU READY?</text>
    </g>

    <g class="date-banner" transform="translate(62,932) rotate(-17)">
      <polygon points="-90,-22 14,-22 14,18 -90,18" fill="var(--red-dark)"/>
      <rect x="0" y="-58" width="560" height="58" fill="var(--red)"/>
      <text class="date-text" x="18" y="-13" font-size="36" fill="var(--white)">SATURDAY, 28<tspan font-size="20" dy="-14">TH</tspan><tspan dy="14"> SEPTEMBER 2013</tspan></text>
    </g>
  </svg>

  <div class="social-bar">
    <span class="social-item"><span class="social-mark"></span>@qarinshore</span>
    <span class="social-item"><span class="social-mark"></span>/qarinshore</span>
    <span class="social-item"><span class="social-mark"></span>info@qarinshore.example</span>
    <span class="social-item"><span class="social-mark"></span>Qarinshore</span>
    <span class="social-item"><span class="social-mark"></span>@qarinshore</span>
  </div>

  <footer class="sponsors">
    <span class="sponsor">Qarin Shore</span>
    <span class="sponsor">Dunmere Regent Hotel</span>
    <span class="sponsor">Dunmere Sahel Hotel</span>
    <span class="sponsor">Tolvik Harbour Raceway</span>
    <span class="sponsor">Fennwood</span>
    <span class="sponsor">Play Orbit</span>
    <span class="sponsor">Halcyon Court Dunmere Isle</span>
    <span class="sponsor">Marrowgate Azure</span>
    <span class="sponsor">Gold Moth</span>
  </footer>
</main>
</body>
</html>
```